Brochure Design

I need a brochure that I can give to prospective clients during meetings and shows. My company website is www.brightpathmarketingpro.com

There is information to help with the creation of the brochure. Additionally, I will be attaching the new company logo. The website is being fixed behind the scenes to incorporate the new logo and color schemes. Please allow the colors in the brochure to the logo and not the current website.

Thanks!

```html
<!DOCTYPE html>
<html lang="en">
<head>
<meta charset="utf-8">
<title>Brightpath – Digital Marketing and SEO Services Brochure</title>
<link href="https://fonts.googleapis.com/css2?family=Exo+2:wght@300;400&family=Montserrat:wght@400;500&family=Cinzel:wght@500&display=swap" rel="stylesheet">
<style>
  :root{
    --blue:#1b6fb8;
    --green:#6cb12a;
    --green-dark:#4d8f17;
    --gray:#6f7073;
    --text:#3a3a3c;
    --paper:#ffffff;
    --backdrop:#e9e9ea;
  }
  *{margin:0;padding:0;box-sizing:border-box}
  html,body{width:1200px;height:801px;overflow:hidden;background:var(--backdrop)}
  .spread{position:absolute;left:32px;top:32px;width:1136px;height:736px;display:flex;box-shadow:0 4px 14px rgba(0,0,0,.25)}
  .page{position:relative;width:568px;height:736px;background:var(--paper);overflow:hidden}
  .page--inside{background:linear-gradient(90deg,#fff 0%,#fff 85%,#e6e6e7 100%)}
  .page--cover{background:linear-gradient(90deg,#e8e8e9 0%,#fff 12%,#fff 100%)}
  .deco{position:absolute;left:0;top:0}
  .headline{position:absolute;left:0;width:568px;top:62px;text-align:center;font:400 16px/20px "Exo 2",sans-serif;color:var(--blue);letter-spacing:.2px}
  .service{position:absolute;width:188px}
  .service__icon{position:absolute;left:-42px;top:-2px}
  .service__title{font:400 14.5px/18px "Exo 2",sans-serif;color:var(--blue);margin-bottom:6px;white-space:nowrap}
  .service__text,.why__text{font:400 7.6px/10px "Montserrat",sans-serif;color:var(--text);text-align:justify}
  .illustration{position:absolute;left:0;top:322px;width:208px;height:214px;background:linear-gradient(135deg,#f2f2f2 0%,#dcdcdd 60%,#a6d36a 100%)}
  .why{position:absolute;left:212px;top:338px;width:318px}
  .why__title{font:400 15px/18px "Exo 2",sans-serif;color:var(--blue);margin-bottom:10px}
  .why__text{margin-bottom:9px}
  .logo-badge{position:absolute;left:36px;top:548px;width:132px;height:96px;border-radius:50%;background:radial-gradient(ellipse at 50% 40%,#fff 55%,#d4d4d5 100%);display:flex;flex-direction:column;align-items:center;justify-content:center;gap:6px}
  .brand-dot{border-radius:50%;background:var(--green)}
  .brand-name{font-family:"Exo 2",sans-serif;font-weight:400;color:var(--green-dark);letter-spacing:3px}
  .contact{position:absolute;left:46px;top:664px;font:400 9.2px/13px "Montserrat",sans-serif;color:#fff}
  .contact li{list-style:none;display:flex;align-items:center;gap:6px}
  .contact .phone{font-weight:500}
  .social{position:absolute;left:420px;top:672px;display:flex;gap:10px}
  .social span{width:40px;height:28px;border-radius:5px;background:linear-gradient(#3d8fd6,#1b5f9e)}
  .cover-logo{position:absolute;left:174px;top:66px;width:220px;display:flex;flex-direction:column;align-items:center;gap:14px}
  .cover-title{position:absolute;left:0;width:568px;top:230px;text-align:center;font:500 22px/26px "Cinzel",serif;color:var(--blue);letter-spacing:.6px}
  .wordcloud{position:absolute;left:30px;top:300px;width:508px;height:320px;border-radius:50%;background:radial-gradient(ellipse at 58% 48%,#eef6e4 0%,#a9d46f 28%,#b4b5b7 52%,#8a8b8e 100%)}
  .cover-url{position:absolute;right:30px;top:705px;font:400 10.5px/13px "Montserrat",sans-serif;color:#fff;display:flex;align-items:center;gap:5px}
</style>
</head>
<body>
<main class="spread">
  <section class="page page--inside">
    <svg class="deco" width="568" height="736" viewBox="0 0 568 736" aria-hidden="true">
      <path d="M0 0 H150 C80 18 30 60 0 120 Z" fill="var(--green)"/>
      <path d="M0 0 H150 C95 10 50 40 18 84 C30 40 70 10 150 0 Z" fill="#a8d36a"/>
      <path d="M0 610 C120 560 260 580 420 640 C480 664 530 680 568 690 V736 H0 Z" fill="var(--gray)"/>
      <path d="M0 600 C120 552 260 572 420 632 C480 656 530 672 568 682 V690 C530 680 480 664 420 640 C260 580 120 560 0 610 Z" fill="#d9d9da"/>
    </svg>

    <h1 class="headline">YOU WANT TO CONNECT WITH MORE CLIENTS.<br>WE HAVE THE SEO TOOLS YOU NEED TO MAKE THAT HAPPEN.</h1>

    <article class="service" style="left:78px;top:122px">
      <svg class="service__icon" width="34" height="34" viewBox="0 0 34 34" aria-hidden="true"><circle cx="17" cy="17" r="12" fill="none" stroke="var(--blue)" stroke-width="5" stroke-dasharray="20 6"/><path d="M27 5 l4 8 -9 0z" fill="#e23a2e"/></svg>
      <h2 class="service__title">Search Engine Optimization</h2>
      <p class="service__text">Brightpath is an SEO company able to provide your business with practical SEO services and Search Engine Optimization solutions to help your business grow.</p>
    </article>
    <article class="service" style="left:343px;top:122px">
      <svg class="service__icon" width="34" height="34" viewBox="0 0 34 34" aria-hidden="true"><rect x="11" y="2" width="10" height="10" fill="#e8a21b"/><rect x="3" y="12" width="10" height="10" fill="#e23a2e"/><rect x="15" y="12" width="10" height="10" fill="var(--green)"/><rect x="9" y="22" width="10" height="10" fill="var(--blue)"/></svg>
      <h2 class="service__title">Advanced SEO Tools</h2>
      <p class="service__text">Brightpath is an SEO company that offers cutting edge SEO tools, SEO marketing, SEO training and Search Engine Optimization solutions in order to attract more web traffic and convert more sales for your business.</p>
    </article>
    <article class="service" style="left:78px;top:220px">
      <svg class="service__icon" width="34" height="34" viewBox="0 0 34 34" aria-hidden="true"><circle cx="17" cy="17" r="13" fill="none" stroke="#e8a21b" stroke-width="5" stroke-dasharray="14 6"/><circle cx="17" cy="17" r="6" fill="var(--blue)"/></svg>
      <h2 class="service__title">Our SEO Services</h2>
      <p class="service__text">Brightpath is an SEO company that helps clients to achieve higher search engine rankings by using SEO tools and providing SEO tips in order to promote business growth.</p>
    </article>
    <article class="service" style="left:343px;top:220px">
      <svg class="service__icon" width="34" height="34" viewBox="0 0 34 34" aria-hidden="true"><rect x="13" y="2" width="8" height="12" fill="#e23a2e"/><rect x="20" y="13" width="12" height="8" fill="var(--blue)"/><rect x="13" y="20" width="8" height="12" fill="#e8c21b"/><rect x="2" y="13" width="12" height="8" fill="var(--green)"/></svg>
      <h2 class="service__title">Beyond our SEO Services</h2>
      <p class="service__text">Brightpath is an SEO company that strongly believes in listening to the customer's Search Engine Optimization goals in order to provide customized SEO Services, SEO Tools and SEO Tips to achieve those goals.</p>
    </article>

    <div class="illustration" role="img" aria-label="Illustration of small figures racing up grey arrows, one green figure leading on a green arrow"></div>

    <article class="why">
      <h2 class="why__title">WHY SEO MARKETING AND<br>SEARCH ENGINE OPTIMIZATION</h2>
      <p class="why__text">In today's business environment, it's really hard to get noticed. There's a lot of competition out there. That's why when it comes to getting an edge; businesses need to be doing everything they can to succeed. Search Engine Optimization can help to cut through all the noise and deliver powerful content to target audiences. Brightpath provides SEO Services and SEO Marketing to help businesses grow by using SEO tools and other SEO tips to successfully improve organic search ranks for their clients.</p>
      <p class="why__text">Call our SEO Company to set up a complimentary search engine optimization consultation, so you can learn how adding SEO Marketing and SEO Services will directly impact your Search Engine Optimization. We can use all of the different SEO tools to have your company ranking higher in search engine results, ultimately promoting higher client traffic to your company's website. That increase will translate into a higher number of converted sales and will directly lead to increased earnings for your business. Brightpath is an experienced SEO Company that can help your business reach its organizational goals.</p>
      <p class="why__text">Follow the link to find out how we can help your organization's Search Engine Optimization and SEO Marketing.</p>
    </article>

    <div class="logo-badge">
      <span class="brand-dot" style="width:30px;height:30px"></span>
      <span class="brand-name" style="font-size:13px">BRIGHTPATH</span>
    </div>

    <ul class="contact">
      <li><svg width="7" height="9" viewBox="0 0 7 9" aria-hidden="true"><path d="M3.5 0 A3.5 3.5 0 0 1 7 3.5 C7 6 3.5 9 3.5 9 S0 6 0 3.5 A3.5 3.5 0 0 1 3.5 0Z" fill="#a6d05f"/></svg>418 Kamani Lane</li>
      <li style="padding-left:13px">Kailua, HI 96734</li>
      <li class="phone" style="margin-top:3px"><svg width="9" height="7" viewBox="0 0 9 7" aria-hidden="true"><path d="M0 2 Q4.5 -1 9 2 L8 3 6 2.4 5.6 1.6 H3.4 L3 2.4 1 3Z M2 3.5 H7 L8 7 H1Z" fill="#a6d05f"/></svg>[808] 555 - 0142</li>
      <li style="margin-top:3px"><svg width="8" height="8" viewBox="0 0 8 8" aria-hidden="true"><circle cx="4" cy="4" r="4" fill="#a6d05f"/></svg>www.brightpathmarketingpro.com</li>
    </ul>

    <div class="social" aria-hidden="true"><span></span><span></span><span></span></div>
  </section>

  <section class="page page--cover">
    <svg class="deco" width="568" height="736" viewBox="0 0 568 736" aria-hidden="true">
      <path d="M60 736 C180 690 380 690 568 648 V736 Z" fill="var(--green)"/>
      <path d="M60 736 C180 682 380 680 568 636 V648 C380 690 180 690 60 736 Z" fill="#c9e3a2"/>
    </svg>

    <div class="cover-logo">
      <span class="brand-dot" style="width:90px;height:90px"></span>
      <span class="brand-name" style="font-size:27px;letter-spacing:5px">BRIGHTPATH</span>
    </div>

    <h2 class="cover-title">Digital Marketing And Seo Services</h2>

    <div class="wordcloud" role="img" aria-label="Word cloud of SEO terms in grey with a magnifying glass enlarging the word SEO in green"></div>

    <p class="cover-url"><svg width="9" height="9" viewBox="0 0 9 9" aria-hidden="true"><circle cx="4.5" cy="4.5" r="4.5" fill="#a6d05f"/></svg>www.brightpathmarketingpro.com</p>
  </section>
</main>
</body>
</html>
```